Clearpath Ledgers New Website

Please review the attached Design Brief with additional details. Thank you!

The goal is to create a website that effectively communicates the benefits of ClearPath Ledgers to eye care professionals. The website should streamline the process of understanding and utilizing ClearPath Ledgers' services, emphasizing improved patient outcomes, increased referrals, and enhanced patient engagement.

Target Market(s)

Eyecare Professionals

Number of Pages Required

4 page

```html
<!DOCTYPE html>
<html lang="en">
<head>
<meta charset="utf-8">
<title>Clearpath Ledgers</title>
<link href="https://fonts.googleapis.com/css2?family=Open+Sans:wght@400;600;700&family=Poppins:wght@300;400;500;600&display=swap" rel="stylesheet">
<style>
:root{
  --navy:#23468a;
  --navy-deep:#102446;
  --ink:#1c1836;
  --orange:#f7a43a;
  --sky:#3aa6d8;
  --teal:#2f8a88;
  --mist:#f3f2f6;
  --text:#333;
  --muted:#8a8a95;
  --white:#fff;
}
*{margin:0;padding:0;box-sizing:border-box}
html,body{width:1200px;height:4240px;overflow:hidden}
body{position:relative;background:var(--white);font-family:"Poppins",sans-serif;color:var(--text)}
.abs{position:absolute}
h1,h2,h3{font-family:"Open Sans",sans-serif}

/* header */
.topbar{left:0;top:0;width:1200px;height:38px}
.topbar-text{font-size:10px;color:var(--white);top:12px;white-space:nowrap}
.social-dot{width:9px;height:9px;background:var(--white);top:14px}
.quote-btn{left:840px;top:10px;width:115px;height:18px;background:var(--teal);color:var(--white);font-size:9px;text-align:center;line-height:18px;letter-spacing:.5px}
.logo{left:78px;top:20px;display:flex;align-items:flex-start;gap:8px}
.logo-mark{width:18px;height:18px;background:var(--navy);margin-top:4px}
.logo-name{font-size:19px;font-weight:500;color:var(--navy);line-height:22px}
.logo-tag{font-size:9px;color:var(--ink);line-height:12px}
.nav{font-size:11px;color:#444}
.nav span{position:absolute;white-space:nowrap}
.nav .active{color:var(--navy);font-weight:600}

/* hero */
.hero-photo{left:0;top:82px;width:1200px;height:708px;background:linear-gradient(100deg,#1d3766 0%,#2c4f80 45%,#4c6a92 70%,#2b4670 100%)}
.hero-label{left:105px;top:258px;font-size:19px;color:var(--white);font-family:"Open Sans",sans-serif}
.hero-title{left:105px;top:288px;font-size:52px;line-height:60px;font-weight:700;color:var(--white)}
.hero-copy{left:105px;top:422px;width:500px;font-size:16px;line-height:30px;color:var(--white)}
.btn{background:var(--orange);color:var(--white);font-size:15px;font-weight:600;display:flex;align-items:center;gap:18px;padding-left:16px;height:45px;width:155px}

/* about */
.label{font-size:12px;color:var(--sky);letter-spacing:.3px;padding-bottom:4px;border-bottom:1px solid var(--sky)}
.about-title{left:614px;top:898px;font-size:40px;line-height:52px;font-weight:600;color:var(--navy)}
.about-sub{left:614px;top:1030px;font-size:19px;color:#222}
.about-copy{left:614px;width:506px;font-size:13px;line-height:22px;color:var(--muted)}

/* services */
.services-bg{left:0;top:1811px;width:1200px;height:847px;background:var(--mist)}
.services-band{left:0;top:1399px;width:1200px;height:412px;background:linear-gradient(90deg,#3b4a66,#56637b 50%,#48556d)}
.section-label-light{font-size:12px;color:var(--white);padding-bottom:6px;border-bottom:2px solid var(--white);letter-spacing:.5px}
.services-title{left:84px;top:1490px;font-size:42px;font-weight:600;color:var(--white)}
.more{left:931px;top:1512px;font-size:16px;color:var(--white)}
.more-btn{left:1075px;top:1503px;width:37px;height:38px;background:var(--white)}
.service-card{top:1600px;width:324px;height:358px;background:var(--white);box-shadow:0 4px 14px rgba(0,0,0,.08)}
.service-photo{position:absolute;left:18px;top:18px;width:288px;height:195px}
.service-icon{position:absolute;left:18px;top:163px;width:50px;height:50px;background:var(--orange)}
.service-name{position:absolute;left:18px;top:241px;font-size:19px;font-weight:500;color:#222}
.service-copy{position:absolute;left:16px;top:285px;width:280px;font-size:13px;line-height:22px;color:var(--muted)}

/* why */
.why-title{left:0;width:1200px;text-align:center;top:2066px;font-size:42px;font-weight:600;color:var(--navy)}
.feature{width:320px;height:106px;background:var(--white);border:1px solid #e4e3ee;border-radius:6px}
.feature h3{position:absolute;top:16px;font-size:19px;font-weight:500;color:#222;white-space:nowrap}
.feature p{position:absolute;top:50px;font-size:12px;line-height:21px;color:var(--muted);width:190px}
.feature-icon{width:58px;height:58px;border-radius:50%;background:var(--white);box-shadow:0 3px 10px rgba(0,0,0,.08)}

/* contact */
.contact-photo{left:0;top:2658px;width:1200px;height:466px;background:linear-gradient(90deg,#1b3463 0%,#2a4776 55%,#6d7f98 100%)}
.contact-title{left:130px;top:2712px;font-size:40px;font-weight:700;color:var(--white)}
.contact-sub{left:133px;top:2773px;font-size:13px;color:var(--white)}
.contact-icon{left:130px;width:48px;height:48px;border-radius:50%;border:2px solid var(--white);background:rgba(255,255,255,.15)}
.contact-key{left:192px;font-size:13px;color:var(--white)}
.contact-val{left:192px;font-size:18px;font-weight:600;color:var(--white);line-height:22px;white-space:nowrap}
.form-box{left:678px;top:2793px;width:391px;height:367px;background:var(--orange)}
.field{left:700px;width:346px;height:38px;background:var(--white);font-size:10px;color:#999;padding:12px 14px}
.submit{left:700px;top:3085px;width:346px;height:36px;background:var(--navy-deep);color:var(--white);font-size:12px;font-weight:600;text-align:center;line-height:36px}

/* testimonials */
.t-title{left:0;width:1200px;text-align:center;top:3254px;font-size:40px;font-weight:600;color:var(--navy)}
.t-card{top:3355px;width:496px;height:255px;background:var(--mist)}
.t-line{position:absolute;left:63px;top:40px;width:2px;height:170px;background:var(--navy)}
.t-quote{position:absolute;left:39px;top:110px;width:50px;height:50px;border-radius:50%;background:var(--navy);border:4px solid var(--white);box-shadow:0 0 0 2px var(--navy);color:var(--orange);font-size:30px;font-weight:700;text-align:center;line-height:52px;font-family:"Open Sans",sans-serif}
.t-stars{position:absolute;left:115px;top:38px;color:#f25a1e;font-size:16px;letter-spacing:5px}
.t-copy{position:absolute;left:115px;top:80px;width:340px;font-size:13px;line-height:23px;color:#666}
.t-name{position:absolute;left:115px;top:172px;font-size:17px;font-weight:600;color:#222}
.t-place{position:absolute;left:115px;top:198px;font-size:12px;color:#555}
.t-avatar{position:absolute;left:400px;top:162px;width:54px;height:54px;border-radius:50%;background:linear-gradient(#c8ccd4,#8b94a3)}
.dot{top:3655px;width:9px;height:9px;border-radius:50%;background:#ddd}

/* footer */
.footer{left:0;top:3740px;width:1200px;height:500px;background:var(--ink)}
.f-head{font-size:14px;font-weight:600;color:var(--white)}
.f-link{font-size:12px;color:#c9c7d8}
.f-copy{font-size:11px;line-height:20px;color:#a9a7bd}
.f-social{top:3957px;width:30px;height:30px;background:#2f2a52}
.f-icon{top:4072px;width:48px;height:48px;border-radius:50%;background:#2f2a52}
.f-key{font-size:14px;font-weight:600;color:var(--white)}
.f-val{font-size:11px;color:#a9a7bd;white-space:nowrap}
</style>
</head>
<body>

<!-- header -->
<svg class="abs topbar" viewBox="0 0 1200 38" aria-hidden="true">
  <path d="M390 0 H1200 V38 H440 C425 38 420 0 390 0Z" fill="#102446"/>
</svg>
<svg class="abs" style="left:468px;top:12px" width="8" height="12" viewBox="0 0 8 12" aria-hidden="true"><path d="M4 0a4 4 0 0 1 4 4c0 3-4 8-4 8S0 7 0 4a4 4 0 0 1 4-4z" fill="#fff"/></svg>
<div class="abs topbar-text" style="left:482px">410 Harbor Lane, Westbrook, 20418</div>
<div class="abs topbar-text" style="left:705px">Follow Us:</div>
<div class="abs social-dot" style="left:765px"></div>
<div class="abs social-dot" style="left:781px"></div>
<div class="abs social-dot" style="left:797px"></div>
<div class="abs quote-btn">GET QUOTATION</div>

<div class="abs logo">
  <div class="logo-mark"></div>
  <div><div class="logo-name">Clearpath Ledgers</div><div class="logo-tag">Empowering Healthcare</div></div>
</div>
<nav class="abs nav" style="left:0;top:53px">
  <span class="active" style="left:448px">Home</span>
  <span style="left:541px">About Us</span>
  <span style="left:629px">Conditions</span>
  <span style="left:722px">Services</span>
  <span style="left:829px">Gallery</span>
  <span style="left:910px">Team</span>
  <span style="left:992px">Contact Us</span>
</nav>

<!-- hero -->
<div class="abs hero-photo" role="img" aria-label="Professional holding a tablet in a busy office with colleagues at desks behind him"></div>
<svg class="abs" style="left:0;top:700px" width="1200" height="100" viewBox="0 0 1200 100" aria-hidden="true">
  <path d="M0 50 C250 5 420 85 700 80 C900 76 1050 40 1200 22 V100 H0Z" fill="#f7a43a"/>
  <path d="M0 58 C250 15 420 95 700 92 C900 90 1060 60 1200 50 V100 H0Z" fill="#fff"/>
</svg>
<div class="abs hero-label">CLEARPATH LEDGERS</div>
<h1 class="abs hero-title">Champions of<br>Clearpath Ledgers</h1>
<p class="abs hero-copy">Lorem ipsum dolor sit amet, consectetur adipiscing elit, sed do eiusmod tempor incididunt ut labore et dolore magna aliqua.</p>
<div class="abs btn" style="left:107px;top:559px">Contact us
  <svg width="16" height="12" viewBox="0 0 16 12" aria-hidden="true"><path d="M0 6h14M9 1l5 5-5 5" stroke="#fff" stroke-width="1.6" fill="none"/></svg></div>

<!-- about -->
<svg class="abs" style="left:100px;top:840px" width="480" height="480" viewBox="0 0 480 480" aria-hidden="true">
  <path d="M10 232 A231 231 0 0 1 470 240" stroke="#23468a" stroke-width="8" fill="none"/>
  <path d="M470 240 A230 230 0 0 1 18 300" stroke="#23468a" stroke-width="3" fill="none"/>
</svg>
<div class="abs" style="left:120px;top:860px;width:440px;height:440px;border-radius:50%;background:linear-gradient(135deg,#3d3a38,#8a7e74 55%,#d8d2cc)" role="img" aria-label="Two colleagues reviewing a tablet together"></div>
<div class="abs label" style="left:614px;top:862px">WHO WE ARE</div>
<h2 class="abs about-title">The team you can trust<br>to get the job done</h2>
<div class="abs about-sub">No fear when your expert is a call away</div>
<p class="abs about-copy" style="top:1072px">Lorem ipsum dolor sit amet, consectetur adipiscing elit, sed do eiusmod temp or incididunt ut labore et dolore magna aliqua. Ut enim ad minim veniam, quis laboris nisi ut aliquip ex ea commodo consequat.</p>
<p class="abs about-copy" style="top:1148px">Lorem ipsum dolor sit amet, consectetur adipiscing elit, sed do eiusmod temp or incididunt ut labore et dolore magna aliqua.</p>
<div class="abs btn" style="left:612px;top:1232px">Contact us
  <svg width="16" height="12" viewBox="0 0 16 12" aria-hidden="true"><path d="M0 6h14M9 1l5 5-5 5" stroke="#fff" stroke-width="1.6" fill="none"/></svg></div>

<!-- services -->
<div class="abs services-bg"></div>
<div class="abs services-band" role="img" aria-label="Dimmed office team at work"></div>
<div class="abs section-label-light" style="left:86px;top:1463px">SERVICES</div>
<h2 class="abs services-title">Services We Provide</h2>
<div class="abs more">More Services</div>
<div class="abs more-btn"><svg width="37" height="38" viewBox="0 0 37 38" aria-hidden="true"><path d="M16 14l5 5-5 5" stroke="#3aa6d8" stroke-width="2" fill="none"/></svg></div>

<div class="abs service-card" style="left:86px">
  <div class="service-photo" role="img" aria-label="Nurse reading a tablet with medical staff behind" style="background:linear-gradient(135deg,#d9dde3,#5f8fa8 60%,#2e5a78)"></div>
  <div class="service-icon"></div>
  <div class="service-name">Health Analytics</div>
  <p class="service-copy">Lorem ipsum dolor sit amet, conse or incididunt ut labore et .</p>
</div>
<div class="abs service-card" style="left:437px">
  <div class="service-photo" role="img" aria-label="Analyst working at a laptop with charts on screen" style="background:linear-gradient(135deg,#2c3e56,#5a6f8a 55%,#9fb0c4)"></div>
  <div class="service-icon"></div>
  <div class="service-name">Outcome Monitoring</div>
  <p class="service-copy">Lorem ipsum dolor sit amet, conse or incididunt ut labore et .</p>
</div>
<div class="abs service-card" style="left:790px">
  <div class="service-photo" role="img" aria-label="Doctors discussing a patient chart" style="background:linear-gradient(135deg,#e4e8ec,#9cb3c8 55%,#4a6a8c)"></div>
  <div class="service-icon"></div>
  <div class="service-name">Engagement Tools</div>
  <p class="service-copy">Lorem ipsum dolor sit amet, conse or incididunt ut labore et .</p>
</div>

<!-- why choose us -->
<div class="abs label" style="left:528px;top:2030px">WHY CHOOSE US</div>
<h2 class="abs why-title">Why Choose Us</h2>
<div class="abs" style="left:402px;top:2158px;width:396px;height:396px;border-radius:50%;background:#e9e8f4"></div>
<div class="abs" style="left:440px;top:2196px;width:320px;height:320px;border-radius:50%;background:#d9d8f0"></div>
<div class="abs" style="left:452px;top:2208px;width:296px;height:296px;border-radius:50%;background:linear-gradient(#c7ccd6,#6c7486)" role="img" aria-label="Smiling businessman in a grey suit with arms crossed"></div>

<div class="abs feature" style="left:80px;top:2184px"><h3 style="left:48px">Innovative Solutions</h3><p style="left:48px">Lorem ipsum dolor sit amet, consectetur adipiscing</p></div>
<div class="abs feature" style="left:80px;top:2330px"><h3 style="left:52px">Cost-Effective</h3><p style="left:52px">Lorem ipsum dolor sit amet, consectetur adipiscing</p></div>
<div class="abs feature" style="left:80px;top:2480px"><h3 style="left:48px">Customization</h3><p style="left:48px">Lorem ipsum dolor sit amet, consectetur adipiscing</p></div>
<div class="abs feature" style="left:797px;top:2184px"><h3 style="left:45px">Proven Track Record</h3><p style="left:45px">Lorem ipsum dolor sit amet, consectetur adipiscing</p></div>
<div class="abs feature" style="left:797px;top:2330px"><h3 style="left:72px">Global Reach</h3><p style="left:72px">Lorem ipsum dolor sit amet, consectetur adipiscing</p></div>
<div class="abs feature" style="left:797px;top:2480px"><h3 style="left:48px">Regulatory Compliance</h3><p style="left:48px">Lorem ipsum dolor sit amet, consectetur adipiscing</p></div>

<div class="abs feature-icon" style="left:378px;top:2208px"></div>
<div class="abs feature-icon" style="left:355px;top:2354px"></div>
<div class="abs feature-icon" style="left:378px;top:2504px"></div>
<div class="abs feature-icon" style="left:758px;top:2208px"></div>
<div class="abs feature-icon" style="left:785px;top:2354px"></div>
<div class="abs feature-icon" style="left:758px;top:2504px"></div>
<svg class="abs" style="left:0;top:0" width="1200" height="2600" viewBox="0 0 1200 2600" aria-hidden="true" fill="none" stroke="#f7a43a" stroke-width="1.6">
  <circle cx="407" cy="2232" r="7"/><path d="M394 2252c2-8 24-8 26 0z"/>
  <path d="M378 2373v-10a3 3 0 0 1 6 0v-6a3 3 0 0 1 6 0v14l4-4a3 3 0 0 1 4 4l-8 10h-12z"/>
  <circle cx="407" cy="2533" r="11"/><path d="M407 2527v6l4 3"/>
  <path d="M787 2225l4 8 9 1-7 6 2 9-8-5-8 5 2-9-7-6 9-1z"/>
  <path d="M804 2395c8-20 20-20 26-6M806 2374a6 6 0 1 0 12 0 6 6 0 1 0-12 0"/>
  <circle cx="787" cy="2533" r="6"/><circle cx="787" cy="2533" r="12" stroke-dasharray="4 3"/>
</svg>

<!-- contact -->
<div class="abs contact-photo" role="img" aria-label="Man working at a laptop in a bright office"></div>
<h2 class="abs contact-title">CONTACT US</h2>
<div class="abs contact-sub">Fill out t the form below to get connected with us.</div>

<div class="abs contact-icon" style="top:2832px"><svg width="44" height="44" viewBox="0 0 44 44" aria-hidden="true"><path d="M15 13l4 0 2 6-3 2a14 14 0 0 0 6 6l2-3 6 2v4c0 1-1 2-2 2-10 0-17-7-17-17 0-1 1-2 2-2z" fill="#fff"/></svg></div>
<div class="abs contact-key" style="top:2833px">Our Phone Number:</div>
<div class="abs contact-val" style="top:2851px;font-size:22px">555 014 2290</div>

<div class="abs contact-icon" style="top:2900px"><svg width="44" height="44" viewBox="0 0 44 44" aria-hidden="true"><path d="M22 10a8 8 0 0 1 8 8c0 6-8 16-8 16s-8-10-8-16a8 8 0 0 1 8-8z" fill="none" stroke="#fff" stroke-width="2"/><circle cx="22" cy="18" r="3" fill="#fff"/></svg></div>
<div class="abs contact-key" style="top:2897px">Our Location:</div>
<div class="abs contact-val" style="top:2915px">Suite 66, 410 Harbor Lane,<br>Westbrook</div>

<div class="abs contact-icon" style="top:2978px"><svg width="44" height="44" viewBox="0 0 44 44" aria-hidden="true"><rect x="12" y="15" width="20" height="14" fill="none" stroke="#fff" stroke-width="2"/><path d="M12 15l10 8 10-8" fill="none" stroke="#fff" stroke-width="2"/></svg></div>
<div class="abs contact-key" style="top:2976px">Our Email Address:</div>
<div class="abs contact-val" style="top:2994px">hello@clearpathledgers.net</div>

<div class="abs form-box"></div>
<div class="abs field" style="top:2812px">Full Name</div>
<div class="abs field" style="top:2860px">Email Address</div>
<div class="abs field" style="top:2908px">Phone Number</div>
<div class="abs field" style="top:2957px;height:113px">Message</div>
<div class="abs submit">SUBMIT</div>

<!-- testimonials -->
<div class="abs label" style="left:541px;top:3218px">TESTIMONIALS</div>
<h2 class="abs t-title">What our clients are saying</h2>

<div class="abs t-card" style="left:92px">
  <div class="t-line"></div><div class="t-quote">“</div>
  <div class="t-stars">★★★★★</div>
  <p class="t-copy">Lorem ipsum dolor sit amet, consectetur adipiscing elit, sed do eiusmod tempor incididunt ut labore et dolore magna aliqua. Ut enim</p>
  <div class="t-name">Maren Holt</div><div class="t-place">Green Valley</div>
  <div class="t-avatar" role="img" aria-label="Portrait of the client"></div>
</div>
<div class="abs t-card" style="left:613px">
  <div class="t-line"></div><div class="t-quote">“</div>
  <div class="t-stars">★★★★★</div>
  <p class="t-copy">Lorem ipsum dolor sit amet, consectetur adipiscing elit, sed do eiusmod tempor incididunt ut labore et dolore magna aliqua. Ut enim</p>
  <div class="t-name">Maren Holt</div><div class="t-place">Green Valley</div>
  <div class="t-avatar" role="img" aria-label="Portrait of the client" style="background:linear-gradient(#e0d6c8,#6b5a48)"></div>
</div>
<div class="abs dot" style="left:566px"></div>
<div class="abs dot" style="left:584px"></div>
<div class="abs dot" style="left:602px;background:none;border:2px solid #f25a1e"></div>
<div class="abs dot" style="left:620px"></div>

<!-- footer -->
<svg class="abs" style="left:0;top:3680px" width="1200" height="80" viewBox="0 0 1200 80" aria-hidden="true">
  <path d="M0 40 C200 0 380 10 600 40 C820 70 1000 55 1200 20 V80 H0Z" fill="#f7a43a"/>
  <path d="M0 70 C200 22 380 28 600 55 C820 80 1000 70 1200 40 V80 H0Z" fill="#1c1836"/>
</svg>
<div class="abs footer"></div>
<div class="abs" style="left:118px;top:3812px;display:flex;align-items:center;gap:8px">
  <div style="width:22px;height:22px;background:var(--navy)"></div>
  <div style="font-size:27px;font-weight:500;color:var(--navy);line-height:30px">Clearpath Ledgers</div>
</div>
<p class="abs f-copy" style="left:125px;top:3890px;width:300px">Lorem ipsum dolor sit amet, consectetur adipiscing elit, sed do eiusmod tempor incididunt ut</p>
<div class="abs f-social" style="left:126px;background:var(--orange)"></div>
<div class="abs f-social" style="left:164px"></div>
<div class="abs f-social" style="left:202px"></div>
<div class="abs f-social" style="left:240px"></div>

<div class="abs f-head" style="left:490px;top:3820px">Quick Links</div>
<div class="abs f-link" style="left:490px;top:3863px;line-height:26px">Home<br>Services<br>About Us<br>Contact<br>Blog<br>Testimonials</div>
<div class="abs f-link" style="left:625px;top:3863px;line-height:26px">Cookies Policy<br>Terms of Use<br>Careers<br>Our Team<br>More</div>

<div class="abs f-head" style="left:826px;top:3820px">Newsletters</div>
<p class="abs f-copy" style="left:826px;top:3858px;width:250px">Lorem ipsum dolor sit amet, consectetur adi piscing elit, sed do eiusmod tempor</p>
<div class="abs" style="left:826px;top:3918px;width:196px;height:48px;background:var(--white);font-size:11px;color:#888;padding:16px 24px">Enter Email Address</div>
<div class="abs" style="left:1022px;top:3918px;width:50px;height:48px;background:var(--orange)"><svg width="50" height="48" viewBox="0 0 50 48" aria-hidden="true"><path d="M21 16l8 8-8 8" stroke="#fff" stroke-width="3" fill="none"/></svg></div>

<div class="abs f-icon" style="left:125px"></div>
<div class="abs f-key" style="left:190px;top:4075px">Address</div>
<div class="abs f-val" style="left:190px;top:4098px">410 Harbor Lane</div>
<div class="abs f-icon" style="left:365px;background:var(--orange)"></div>
<div class="abs f-key" style="left:430px;top:4075px">Email Us</div>
<div class="abs f-val" style="left:428px;top:4098px">support@clearpathledgers.net</div>
<div class="abs f-icon" style="left:632px"></div>
<div class="abs f-key" style="left:697px;top:4075px">Contact Us</div>
<div class="abs f-val" style="left:697px;top:4098px">+1 (555) 014 2290</div>
<div class="abs f-icon" style="left:860px"></div>
<div class="abs f-key" style="left:924px;top:4075px">Opening Hour</div>
<div class="abs f-val" style="left:924px;top:4098px">Mon - Friday 10 am - 8pm</div>
<svg class="abs" style="left:0;top:4072px" width="1200" height="48" viewBox="0 0 1200 48" aria-hidden="true" fill="none" stroke="#fff" stroke-width="1.6">
  <path d="M149 14a7 7 0 0 1 7 7c0 5-7 13-7 13s-7-8-7-13a7 7 0 0 1 7-7z"/>
  <rect x="380" y="17" width="18" height="13"/><path d="M380 17l9 7 9-7"/>
  <path d="M648 15h4l2 5-3 2a11 11 0 0 0 5 5l2-3 5 2v4c-9 1-16-6-15-15z" fill="#fff" stroke="none"/>
  <circle cx="884" cy="24" r="9"/><path d="M884 19v5l3 2"/>
</svg>
<div class="abs" style="left:125px;top:4190px;width:950px;height:1px;background:#34304f"></div>
<div class="abs" style="left:0;top:4208px;width:1200px;text-align:center;font-size:11px;font-weight:500;color:var(--white);letter-spacing:.5px">CLEARPATH LEDGERS</div>

</body>
</html>
```